Retail Seafood business needs package/label design

In need of packaging/label design for multiple seafood products such as sword fish, halibut, cod fish, scallops, mahi, catfish, and lobster tails

```html
<!DOCTYPE html>
<html lang="en">
<head>
<meta charset="UTF-8">
<title>Seafood Lobster Tails Label</title>
<link href="https://fonts.googleapis.com/css2?family=Bebas+Neue&family=Oswald:wght@300;500&display=swap" rel="stylesheet">
<style>
  :root {
    --backdrop: #e8e8e8;
    --label-paper: #f4f4f4;
    --ink: #1c1c1c;
    --ribbon: #222222;
    --ribbon-text: #f4f4f4;
    --art-light: #e2e2e2;
    --art-dark: #b9b9b9;
  }
  * { margin: 0; padding: 0; box-sizing: border-box; }
  html, body {
    width: 1200px;
    height: 830px;
    overflow: hidden;
    background: var(--backdrop);
  }
  .canvas {
    position: relative;
    width: 1200px;
    height: 830px;
  }
  .label {
    position: absolute;
    left: 387px;
    top: 34px;
    width: 425px;
    height: 762px;
    background: var(--label-paper);
    color: var(--ink);
  }
  .fresh-ribbon {
    position: absolute;
    left: 325px;
    top: 0;
    width: 81px;
    height: 80px;
  }
  .fresh-ribbon__text {
    position: absolute;
    left: 0;
    top: 18px;
    width: 81px;
    text-align: center;
    font-family: "Oswald", sans-serif;
    font-weight: 500;
    font-size: 19px;
    letter-spacing: 1px;
    color: var(--ribbon-text);
  }
  .headline {
    position: absolute;
    left: 0;
    top: 100px;
    width: 425px;
    height: 130px;
  }
  .headline text {
    font-family: "Oswald", sans-serif;
    font-weight: 500;
    font-size: 64px;
    letter-spacing: 14px;
    fill: var(--ink);
  }
  .product-name {
    position: absolute;
    left: 0;
    top: 200px;
    width: 425px;
    text-align: center;
    font-family: "Oswald", sans-serif;
    font-weight: 300;
    font-size: 26px;
    letter-spacing: 0.5px;
  }
  .lobster-art {
    position: absolute;
    left: 90px;
    top: 245px;
    width: 250px;
    height: 195px;
    border-radius: 6px;
    background: radial-gradient(ellipse at center, var(--art-dark) 0%, var(--art-light) 70%, var(--label-paper) 100%);
  }
  .tagline {
    position: absolute;
    left: 0;
    top: 560px;
    width: 425px;
    text-align: center;
    font-family: "Bebas Neue", sans-serif;
    font-size: 25px;
    line-height: 27px;
    letter-spacing: 3.5px;
  }
</style>
</head>
<body>
<div class="canvas">
  <div class="label">
    <div class="fresh-ribbon">
      <svg width="81" height="80" viewBox="0 0 81 80" aria-hidden="true">
        <polygon points="0,0 81,0 81,80 40.5,62 0,80" fill="var(--ribbon)"/>
      </svg>
      <span class="fresh-ribbon__text">FRESH</span>
    </div>

    <svg class="headline" viewBox="0 0 425 130" aria-label="Seafood">
      <defs>
        <path id="headline-arc" d="M 30 118 Q 212 10 395 118"/>
      </defs>
      <text text-anchor="middle">
        <textPath href="#headline-arc" startOffset="50%">SEAFOOD</textPath>
      </text>
    </svg>

    <div class="product-name">LOBSTER TAILS</div>

    <div class="lobster-art" role="img" aria-label="Hand-drawn black ink illustration of a lobster"></div>

    <p class="tagline">Authentic Seafood<br>Straight From<br>The Ocean</p>
  </div>
</div>
</body>
</html>
```